Retro game shop business card design

We need a card designed both front and back. we already have a logo. The business name is called Brisk Copper Atlas and we work on customizing and modifying old velmora zuma tabs. Our website is briskcopperatlas.com

our business cards are often shown in glintly posts ans should be designed so that you can easy identify and see in am image. @briskcopperatlas.

Target Market(s)

men 13-40

Contact Information for Business Card

should have logo, wesbite, and if possible some artwork related to zuma tab mods

Font styles to use
Sans Serif

Colors

Designer to choose colors to be used in the design.

Requirements
Must have
• logo, website url www.briskcopperatlas.com, hastag #zumatabmods, email, support@briskcopperatlas.com. zuma tab imagry only (illustration preffered)
Nice to have
• illustrations, graphic design with zuma tab mods (see glintly #zumatabmods)
Should not have
• childlike depictions of zumatabs, kids, anything unrelated to zuma tab mods, no hands, no bertil, no pixel art

```html
<!DOCTYPE html>
<html lang="en">
<head>
<meta charset="utf-8">
<title>Brisk Copper Atlas — Business Card</title>
<link href="https://fonts.googleapis.com/css2?family=Lato:wght@400;700;900&display=swap" rel="stylesheet">
<style>
  :root {
    --stage: #3a3533;
    --card: #050505;
    --accent: #6b74d6;
    --accent-soft: #3f4690;
    --text-grey: #8a8a8a;
    --logo-grey: #cfcfcf;
    --art-light: #d9d9d9;
    --art-mid: #7d86c9;
  }
  * { box-sizing: border-box; margin: 0; padding: 0; }
  html, body { width: 1200px; height: 847px; overflow: hidden; }
  body {
    background: var(--stage);
    font-family: "Lato", sans-serif;
    display: flex;
    align-items: center;
    justify-content: center;
    gap: 50px;
  }
  .card {
    position: relative;
    width: 525px;
    height: 300px;
    background: var(--card);
    box-shadow: 0 18px 40px rgba(0,0,0,0.45);
  }
  /* Front */
  .card-front .mascot-art {
    position: absolute;
    left: 50%;
    top: 36px;
    width: 150px;
    height: 170px;
    transform: translateX(-50%);
    border-radius: 14px;
    background: linear-gradient(160deg, var(--art-light) 0%, #9a9a9a 55%, var(--art-mid) 100%);
  }
  .hashtag {
    color: var(--accent);
    font-size: 15px;
    letter-spacing: 4px;
    font-weight: 400;
  }
  .card-front .hashtag {
    position: absolute;
    left: 0; right: 0;
    top: 228px;
    text-align: center;
  }
  /* Back */
  .card-back .brand {
    position: absolute;
    left: 30px;
    top: 92px;
    width: 200px;
    display: flex;
    align-items: center;
    gap: 10px;
  }
  .brand-mark {
    width: 14px; height: 14px;
    background: var(--logo-grey);
    flex: none;
  }
  .brand-name {
    color: var(--logo-grey);
    font-weight: 900;
    font-size: 24px;
    line-height: 1.05;
    text-transform: uppercase;
    letter-spacing: 1px;
  }
  .card-back .hashtag {
    position: absolute;
    left: 40px;
    top: 228px;
    width: 180px;
    text-align: center;
  }
  .divider {
    position: absolute;
    left: 252px;
    top: 38px;
    width: 1.5px;
    height: 200px;
    background: var(--accent-soft);
  }
  .contact {
    position: absolute;
    left: 272px;
    top: 50px;
    color: var(--text-grey);
    font-size: 14px;
    line-height: 1.35;
  }
  .person-name {
    color: var(--accent);
    font-weight: 700;
    font-size: 22px;
    letter-spacing: 0.5px;
  }
  .person-title { margin-bottom: 8px; }
  .address { margin-bottom: 6px; }
  .contact-row { display: flex; align-items: center; gap: 10px; }
  .contact-row svg { width: 13px; height: 13px; flex: none; }
  .web-domain { color: var(--accent); }
</style>
</head>
<body>
  <section class="card card-front">
    <div class="mascot-art" role="img" aria-label="Illustration of a handheld game console mascot in a top hat, holding a cane"></div>
    <p class="hashtag">#zumatabmods</p>
  </section>

  <section class="card card-back">
    <div class="brand">
      <span class="brand-mark"></span>
      <span class="brand-name">Brisk Copper Atlas</span>
    </div>
    <p class="hashtag">#zumatabmods</p>
    <div class="divider"></div>
    <div class="contact">
      <p class="person-name">ARLO FENWICK</p>
      <p class="person-title">Founder &amp; CEO</p>
      <p>1234 First Line Address</p>
      <p class="address">5678 Second Line Address</p>
      <p class="contact-row">
        <svg viewBox="0 0 16 16"><path fill="var(--accent)" d="M3 1l3 3-1.5 2c1 2 3 4 5 5l2-1.5 3 3-2 2C7 14 2 9 1 3z"/></svg>
        5550148213
      </p>
      <p class="contact-row">
        <svg viewBox="0 0 16 16"><rect x="1" y="3" width="14" height="10" fill="var(--accent)"/><path d="M1 3l7 6 7-6" stroke="var(--card)" stroke-width="1.4" fill="none"/></svg>
        support@briskcopperatlas.com
      </p>
      <p class="contact-row">
        <svg viewBox="0 0 16 16"><circle cx="8" cy="8" r="7" fill="var(--accent)"/><path d="M1 8h14M8 1v14M3 4h10M3 12h10" stroke="var(--card)" stroke-width="1"/></svg>
        <span>www.<span class="web-domain">briskcopperatlas</span>.com</span>
      </p>
    </div>
  </section>
</body>
</html>
```